FREE DENTURES

The card will be placed on plastic stand at doctors office and Seniors centers. This is to acheive specific market segment of people that must have Evergard A & B card and FULL helpnet.
The size of the card shuold be 3.1/2" X 6" printed on vertical format. The basic design must have a picture of a denture and a eye glass frame.The content should be:
NEED DENTURES and/or EYE GLASSES?
NO COST TO YOU
Must have EVERGARD A & B and FULL HELPNET
Must qualify for program
No obligation Call today
BRAM OKUDA 555-238-0194
(Not affiliated with Norvale Union Authority, the Federal Evergard or the State Helpnet Program

Add at a proper side or top. 2 stripes, 1 Red, 1 blue in a waive format.

```html
<!DOCTYPE html>
<html lang="en">
<head>
<meta charset="utf-8">
<title>Need Dentures and/or Eye Glasses? – Rack Card</title>
<link rel="stylesheet" href="https://fonts.googleapis.com/css2?family=Oswald:wght@400;500;600;700&family=Roboto+Condensed:wght@400;700&display=swap">
<style>
  :root{
    --bg:#2a2a2a;
    --paper:#f3f5f7;
    --blue:#1c76bb;
    --blue-dark:#12548e;
    --blue-light:#2f9be0;
    --white:#ffffff;
    --ink:#333b44;
    --photo-a:#c9d3da;
    --photo-b:#8fb1c4;
  }
  *{margin:0;padding:0;box-sizing:border-box}
  html,body{width:806px;height:1200px;overflow:hidden;background:var(--bg)}
  .card{
    position:absolute;left:95px;top:75px;width:615px;height:1030px;
    background:var(--paper);overflow:hidden;
    font-family:"Oswald",sans-serif;
  }
  .top-band{position:absolute;left:0;top:0;width:100%;height:70px;background:var(--blue)}
  .top-band::after{content:"";position:absolute;left:0;right:0;top:54px;height:3px;background:var(--white)}
  .headline-ribbon{position:absolute;left:70px;top:22px;width:475px;height:62px;z-index:3}
  .headline-ribbon svg{position:absolute;inset:0}
  .headline-ribbon h1{
    position:relative;font-weight:500;font-size:26px;color:var(--white);
    text-align:center;line-height:62px;letter-spacing:.5px;white-space:nowrap;
  }
  .photo{
    position:absolute;left:0;top:70px;width:100%;height:330px;
    background:linear-gradient(120deg,var(--photo-b) 0%,var(--photo-a) 45%,#e8d6c8 70%,var(--photo-a) 100%);
  }
  .chevron{position:absolute;left:0;top:290px;width:615px;height:290px;z-index:2}
  .no-cost{
    position:absolute;left:62px;top:398px;z-index:3;white-space:nowrap;
    font-weight:700;font-size:62px;color:var(--white);letter-spacing:.5px;
    text-shadow:0 3px 4px rgba(0,0,0,.35);
  }
  .requirement{position:absolute;left:215px;top:525px;width:400px;height:106px}
  .requirement svg{position:absolute;inset:0}
  .requirement p{
    position:relative;padding:12px 0 0 38px;font-weight:400;font-size:31px;
    line-height:41px;color:var(--white);white-space:nowrap;
  }
  .qualify{
    position:absolute;right:28px;top:642px;text-align:right;white-space:nowrap;
    font-family:"Roboto Condensed",sans-serif;font-weight:700;font-size:50px;
    line-height:52px;color:var(--blue);
  }
  .bottom-band{position:absolute;left:0;top:942px;width:100%;height:88px;background:var(--blue-dark)}
  .icon-badge{
    position:absolute;left:45px;width:126px;height:126px;border-radius:50%;
    background:var(--white);box-shadow:0 2px 6px rgba(0,0,0,.25);z-index:2;
  }
  .icon-badge svg{position:absolute;inset:6px}
  .badge-glasses-round{top:594px}
  .badge-tooth{top:740px}
  .badge-glasses-square{top:882px}
  .product{
    position:absolute;top:773px;height:92px;border:6px solid var(--blue);
    border-radius:6px;background:var(--white);box-shadow:0 2px 5px rgba(0,0,0,.25);
  }
  .product .fill{width:100%;height:100%}
  .product-frames-a{left:210px;width:105px}
  .product-frames-a .fill{background:linear-gradient(#f4f4f4,#d9d6d0)}
  .product-denture{left:337px;width:114px}
  .product-denture .fill{background:linear-gradient(#f4e9e6,#e59a9a 60%,#f2ece5)}
  .product-frames-b{left:472px;width:115px}
  .product-frames-b .fill{background:linear-gradient(#f7f7f7,#cfd2d4)}
  .disclaimer{
    position:absolute;right:25px;top:888px;width:395px;text-align:right;
    font-family:"Roboto Condensed",sans-serif;font-size:13px;line-height:16px;color:var(--ink);
  }
  .call{
    position:absolute;right:25px;top:952px;z-index:3;color:var(--white);
    font-weight:400;text-align:right;white-space:nowrap;
  }
  .call .lead{font-size:28px;line-height:36px}
  .call .agent{display:flex;align-items:center;justify-content:flex-end;gap:12px;font-size:30px;line-height:40px}
  .call .number{font-size:33px}
  .call svg{width:26px;height:26px;flex:none}
</style>
</head>
<body>
<main class="card">
  <div class="top-band"></div>
  <div class="headline-ribbon">
    <svg viewBox="0 0 475 62" preserveAspectRatio="none"><polygon points="18,0 457,0 475,31 457,62 18,62 0,31" fill="var(--blue-light)"/></svg>
    <h1>NEED DENTURES AND/OR EYE GLASSES?</h1>
  </div>

  <div class="photo" role="img" aria-label="Photo of a dentist in mask and scrubs examining a smiling woman's teeth in a dental chair"></div>

  <svg class="chevron" viewBox="0 0 615 290">
    <polygon points="0,100 305,100 615,18 615,170 110,285 0,190" fill="var(--blue-light)"/>
    <polygon points="0,96 300,96 615,14 615,158 110,272 0,178" fill="var(--blue)"/>
    <polygon points="0,102 615,102 615,150 110,262 0,172" fill="var(--blue-dark)" opacity=".35"/>
  </svg>
  <div class="no-cost">NO COST TO YOU</div>

  <div class="requirement">
    <svg viewBox="0 0 400 106" preserveAspectRatio="none"><polygon points="24,0 400,0 400,106 24,106 0,53" fill="var(--blue-dark)"/></svg>
    <p>MUST HAVE EVERGARD A &amp;<br>B AND FULL HELPNET</p>
  </div>

  <p class="qualify">Must qualify for<br>program</p>

  <div class="bottom-band"></div>

  <div class="icon-badge badge-glasses-round">
    <svg viewBox="0 0 114 114" fill="none" stroke="var(--white)" stroke-width="3">
      <circle cx="57" cy="57" r="55" fill="var(--blue)" stroke="none"/>
      <circle cx="57" cy="57" r="47" stroke-width="2"/>
      <circle cx="40" cy="62" r="12"/><circle cx="74" cy="62" r="12"/>
      <path d="M52 60q5-5 10 0M28 60l-6-10M86 60l6-10"/>
    </svg>
  </div>
  <div class="icon-badge badge-tooth">
    <svg viewBox="0 0 114 114" fill="none" stroke="var(--white)" stroke-width="3">
      <circle cx="57" cy="57" r="55" fill="var(--blue)" stroke="none"/>
      <circle cx="57" cy="57" r="47" stroke-width="2"/>
      <path d="M45 33c-10 0-13 10-11 20 2 8 5 12 6 20 1 8 3 13 6 13 4 0 4-14 11-14s7 14 11 14c3 0 5-5 6-13 1-8 4-12 6-20 2-10-1-20-11-20-5 0-8 3-12 3s-7-3-11-3z"/>
    </svg>
  </div>
  <div class="icon-badge badge-glasses-square">
    <svg viewBox="0 0 114 114" fill="none" stroke="var(--white)" stroke-width="3">
      <circle cx="57" cy="57" r="55" fill="var(--blue)" stroke="none"/>
      <circle cx="57" cy="57" r="47" stroke-width="2"/>
      <path d="M25 52h28v10a9 9 0 0 1-9 9h-10a9 9 0 0 1-9-9zM61 52h28v10a9 9 0 0 1-9 9h-10a9 9 0 0 1-9-9zM53 55h8M25 52l5-12M89 52l-5-12"/>
    </svg>
  </div>

  <div class="product product-frames-a"><div class="fill" role="img" aria-label="Photo of a pair of tortoiseshell eyeglass frames"></div></div>
  <div class="product product-denture"><div class="fill" role="img" aria-label="Photo of a full denture set"></div></div>
  <div class="product product-frames-b"><div class="fill" role="img" aria-label="Photo of black eyeglass frames"></div></div>

  <p class="disclaimer">(Not affiliated with Norvale Union Authority, the Federal Evergard or the State Helpnet Program)</p>

  <div class="call">
    <p class="lead">NO OBLIGATION CALL TODAY</p>
    <p class="agent"><span>BRAM OKUDA</span>
      <svg viewBox="0 0 26 26"><rect width="26" height="26" rx="5" fill="var(--white)"/><path d="M8 5l3 4-2 2c1 3 3 5 6 6l2-2 4 3-2 3c-7 0-13-6-13-13z" fill="var(--blue-dark)"/></svg>
      <span class="number">555-238-0194</span>
    </p>
  </div>
</main>
</body>
</html>
```